Business Cards, Letterhead and Email signature for Halvern Building Collective
Halvern Building Collective
Professional
Doran Pellick
Partner
Office: 4100 Birchmont Ave Suite 900 Charlotte, NC 28211
Mailing: 5217 Birchmont Ave #482 Charlotte, NC 28211
dpellick@halvernbuildingcoll.example
halvvernbuildingcoll.example
I am open to ideas, maybe the logo with a matching background color. Be creative

```html
<!DOCTYPE html>
<html lang="en">
<head>
<meta charset="UTF-8">
<title>Halvern Building Collective — Stationery</title>
<link rel="stylesheet" href="https://fonts.googleapis.com/css2?family=Montserrat:wght@700&family=Open+Sans:wght@400;600&display=swap">
<style>
  :root {
    --navy: #0f2a66;
    --blue: #1f4fa8;
    --sky: #5d86cf;
    --paper: #ffffff;
    --ink: #3a3f4a;
    --muted: #7a818e;
    --stage: #e8eaee;
  }
  * { margin: 0; padding: 0; box-sizing: border-box; }
  html, body { width: 1200px; height: 698px; overflow: hidden; }
  body {
    background: var(--stage);
    font-family: "Open Sans", Arial, sans-serif;
    color: var(--ink);
    position: relative;
  }
  .sheet {
    position: absolute;
    background: var(--paper);
    box-shadow: 0 4px 14px rgba(0,0,0,.14);
    overflow: hidden;
  }
  .band {
    position: absolute;
    left: 0; bottom: 0;
    width: 100%;
    background: linear-gradient(180deg, var(--sky), var(--navy));
  }
  .brand {
    display: flex;
    align-items: center;
    gap: 6px;
    font-family: "Montserrat", Arial, sans-serif;
    font-weight: 700;
    color: var(--navy);
    text-transform: uppercase;
    letter-spacing: .04em;
    line-height: 1.1;
    white-space: nowrap;
  }
  .brand-mark { background: var(--navy); flex: none; }

  /* Letterhead */
  .letterhead { left: 60px; top: 38px; width: 440px; height: 622px; }
  .letterhead .brand { position: absolute; top: 30px; right: 32px; font-size: 12px; }
  .letterhead .brand-mark { width: 16px; height: 16px; }
  .letterhead .contact {
    position: absolute; top: 60px; right: 32px;
    text-align: right; font-size: 7px; color: var(--muted); line-height: 1.5;
  }
  .letter-body {
    position: absolute; top: 130px; left: 40px; right: 40px;
    font-size: 8.5px; line-height: 1.7;
  }
  .letter-body p { margin-bottom: 10px; }
  .letter-body .sign { margin-top: 18px; font-weight: 600; color: var(--navy); }
  .letter-body .sign-role { font-weight: 400; color: var(--muted); }
  .letterhead .band { height: 80px; }

  /* Envelope */
  .envelope { left: 540px; top: 38px; width: 600px; height: 300px; }
  .envelope .brand { position: absolute; top: 24px; left: 28px; font-size: 12px; }
  .envelope .brand-mark { width: 16px; height: 16px; }
  .envelope .return {
    position: absolute; top: 46px; left: 50px;
    font-size: 7px; color: var(--muted); line-height: 1.5;
  }
  .envelope .band { height: 60px; }

  /* Business cards */
  .card { width: 290px; height: 166px; top: 400px; }
  .card-front { left: 540px; }
  .card-front .brand { position: absolute; top: 16px; right: 16px; font-size: 8px; }
  .card-front .brand-mark { width: 11px; height: 11px; }
  .card-front .person { position: absolute; top: 48px; left: 18px; }
  .person-name { font-size: 12px; font-weight: 600; color: var(--navy); }
  .person-role { font-size: 8px; color: var(--muted); margin-bottom: 7px; }
  .person-details { font-size: 6.5px; line-height: 1.55; }
  .card-front .band { height: 26px; }

  .card-back {
    left: 850px;
    background: linear-gradient(160deg, var(--blue), var(--navy));
  }
  .card-back .brand {
    position: absolute; right: 16px; bottom: 16px;
    font-size: 9px; color: var(--paper);
  }
  .card-back .brand-mark { width: 12px; height: 12px; background: var(--paper); }
</style>
</head>
<body>

<section class="sheet letterhead">
  <div class="brand"><span class="brand-mark"></span>Halvern Building Collective</div>
  <div class="contact">
    Office: 4100 Birchmont Ave Suite 900 Charlotte, NC 28211<br>
    Mailing: 5217 Birchmont Ave #482 Charlotte, NC 28211<br>
    dpellick@halvernbuildingcoll.example<br>
    halvvernbuildingcoll.example
  </div>
  <div class="letter-body">
    <p>March 4, 2025</p>
    <p>Dear Client,</p>
    <p>Thank you for choosing us for your next project. Our team will share a full schedule and cost outline within the coming week.</p>
    <p>We look forward to building something lasting together.</p>
    <p>Sincerely,</p>
    <p class="sign">Doran Pellick<br><span class="sign-role">Partner</span></p>
  </div>
  <div class="band" role="img" aria-label="Decorative blue footer band"></div>
</section>

<section class="sheet envelope">
  <div class="brand"><span class="brand-mark"></span>Halvern Building Collective</div>
  <div class="return">
    5217 Birchmont Ave #482<br>
    Charlotte, NC 28211
  </div>
  <div class="band" role="img" aria-label="Decorative blue footer band"></div>
</section>

<section class="sheet card card-front">
  <div class="brand"><span class="brand-mark"></span>Halvern Building Collective</div>
  <div class="person">
    <div class="person-name">Doran Pellick</div>
    <div class="person-role">Partner</div>
    <div class="person-details">
      Tel 704.555.0148<br>
      4100 Birchmont Ave Suite 900 Charlotte, NC 28211<br>
      dpellick@halvernbuildingcoll.example<br>
      halvvernbuildingcoll.example
    </div>
  </div>
  <div class="band" role="img" aria-label="Decorative blue footer band"></div>
</section>

<section class="sheet card card-back" role="img" aria-label="Blue card back with company name">
  <div class="brand"><span class="brand-mark"></span>Halvern Building Collective</div>
</section>

</body>
</html>
```